A professional oriented Health and Safety company is in need of a postcard design

Hello we need a postcard to draw business to our company Brisk Lantern LLC. We are a health and safety based company providing education and testing. The main focuses we offer are CPR and AED training for Health Care Providers and the general public, First Aid training, Bloodborne Pathogens training, and Respirator and N95 fit testing. We would like to see a professional looking postcard that reflects a lot on education. No cartoonist postcards please keep it crisp and clean. We have been in business since 2007 and can host large classes. We are educating and testing throughout the State of Michigan. Target audiences are Medical and Dental professionals, Child Care centers, Construction and Industrial. Please reference the telephone number and web site on the attached card and include in the postcard.

Some items we would like to see targeted in one way or another are as follows:
-We can train at the business inquiring making scheduling easy for all employees cutting overall costs. Off site training also available
-All training is by licensed healthcare providers
-We use clean and full functioning equipment with the latest technology available
-Pricing is typically lower than having to get educated at yearly conferences
-Courses meet State and OSHA requirements

We have attached some files with our current logo and a business card. We will consider projects with and without the logo. Please focus on the above not what's on the card.
Updates

Industry/Entity Type

Education

Requirements
Nice to have
• Pictures of Medical professionals

```html
<!DOCTYPE html>
<html lang="en">
<head>
<meta charset="utf-8">
<title>Brisk Lantern – Health and Safety Postcard</title>
<link rel="stylesheet" href="https://fonts.googleapis.com/css2?family=Tinos&family=Questrial&display=swap">
<style>
  :root {
    --page-bg: #e9e7e4;
    --card-white: #ffffff;
    --brand-red: #9b1b1e;
    --ink: #1f1f1f;
    --ink-soft: #3a3a3a;
    --rule-grey: #c9c9c9;
    --stamp-grey: #d4d4d4;
    --panel-blue: rgba(221, 232, 239, 0.82);
    --sky-blue: #b9d3e3;
    --sky-pale: #dbe8f0;
    --skin-warm: #f0d2c4;
    --skin-light: #f8e9e2;
    --fire-red: #c2432a;
    --fire-orange: #f29a55;
    --smoke-grey: #d9d2cc;
    --scrubs-teal: #7fb3c4;
    --ward-white: #e8eef1;
    --tactical-dark: #23272d;
    --tactical-mid: #6f757d;
  }
  * { box-sizing: border-box; margin: 0; padding: 0; }
  html, body {
    width: 1200px; height: 875px; overflow: hidden;
    background: var(--page-bg);
  }
  .sheet { position: relative; width: 1200px; height: 875px; }

  .postcard {
    position: absolute;
    width: 600px; height: 408px;
    background: var(--card-white);
    box-shadow: 0 2px 8px rgba(0,0,0,0.15);
    overflow: hidden;
  }
  .postcard--back { left: 300px; top: 20px; }
  .postcard--front { left: 300px; top: 447px; }

  /* Address side */
  .brand {
    position: absolute; left: 22px; top: 110px;
    font-family: "Tinos", "Times New Roman", serif;
  }
  .brand__name { color: var(--brand-red); font-size: 23px; line-height: 1.1; }
  .brand__tagline { color: var(--ink); font-size: 17px; line-height: 1.2; }
  .contact {
    position: absolute; left: 22px; top: 178px;
    font-family: "Questrial", "Century Gothic", sans-serif;
    color: var(--ink); font-size: 13px; line-height: 1.35;
  }
  .contact__person { font-weight: 700; letter-spacing: 0.3px; }
  .contact__details { color: var(--ink-soft); }
  .stamp-box {
    position: absolute; right: 26px; top: 20px;
    width: 104px; height: 104px;
    border: 2px solid var(--stamp-grey);
    display: flex; align-items: center; justify-content: center;
    text-align: center;
    font-family: "Questrial", sans-serif; font-weight: 700;
    font-size: 11px; line-height: 1.35; color: var(--stamp-grey);
    text-transform: uppercase;
  }
  .divider {
    position: absolute; left: 300px; top: 200px;
    width: 1px; height: 190px; background: var(--rule-grey);
  }
  .address-lines { position: absolute; left: 325px; top: 270px; width: 250px; }
  .address-lines span {
    display: block; height: 1px; background: var(--rule-grey); margin-bottom: 28px;
  }

  /* Promotional side */
  .photo-column {
    position: absolute; left: 8px; top: 6px; width: 185px; height: 396px;
    display: flex; flex-direction: column; gap: 6px;
  }
  .photo { width: 100%; }
  .photo--firefighters {
    height: 118px;
    background:
      radial-gradient(ellipse 60% 70% at 70% 60%, var(--fire-orange), transparent 70%),
      linear-gradient(100deg, var(--fire-red) 0%, #d9623a 40%, var(--smoke-grey) 100%);
  }
  .photo--clinical {
    height: 146px;
    background:
      radial-gradient(ellipse 50% 40% at 55% 80%, var(--ward-white), transparent 75%),
      linear-gradient(170deg, #cfd9dd 0%, var(--scrubs-teal) 45%, #9cc3cf 70%, var(--ward-white) 100%);
  }
  .photo--responders {
    height: 120px;
    background:
      radial-gradient(ellipse 40% 60% at 85% 40%, #c9ccd0, transparent 70%),
      linear-gradient(135deg, var(--tactical-dark) 0%, #3b4148 55%, var(--tactical-mid) 100%);
  }
  .hero-photo {
    position: absolute; left: 202px; top: 0; right: 0; bottom: 0;
    background:
      radial-gradient(ellipse 38% 55% at 78% 72%, var(--skin-warm), transparent 72%),
      radial-gradient(ellipse 30% 40% at 92% 90%, var(--skin-light), transparent 75%),
      linear-gradient(180deg, var(--sky-blue) 0%, var(--sky-pale) 60%, #e6eef3 100%);
  }
  .benefits-panel {
    position: absolute; left: 202px; top: 0; width: 195px; height: 408px;
    background: var(--panel-blue);
    border-left: 3px solid var(--card-white);
    padding: 62px 12px 0 14px;
  }
  .benefits {
    list-style: none;
    font-family: "Questrial", "Century Gothic", sans-serif;
    font-size: 12.5px; line-height: 1.45; color: var(--ink-soft);
  }
  .benefits li { position: relative; padding-left: 10px; margin-bottom: 7px; }
  .benefits li::before { content: "•"; position: absolute; left: 0; }
</style>
</head>
<body>
<main class="sheet">

  <section class="postcard postcard--back" aria-label="Postcard address side">
    <div class="stamp-box">Place<br>a postage<br>stamp<br>here.</div>
    <header class="brand">
      <div class="brand__name">Brisk Lantern</div>
      <div class="brand__tagline">Health and Safety Instructors</div>
    </header>
    <div class="contact">
      <div class="contact__person">Owen Halvorsen • Owner-Instructor</div>
      <div class="contact__details">555-014-2286 • www.brisklantern.org</div>
    </div>
    <div class="divider"></div>
    <div class="address-lines"><span></span><span></span><span></span><span></span></div>
  </section>

  <section class="postcard postcard--front" aria-label="Postcard promotional side">
    <div class="photo-column">
      <div class="photo photo--firefighters" role="img" aria-label="Photo of firefighters in protective gear near flames"></div>
      <div class="photo photo--clinical" role="img" aria-label="Photo of medical staff practising CPR on a training manikin"></div>
      <div class="photo photo--responders" role="img" aria-label="Photo of tactical responders in helmets"></div>
    </div>
    <div class="hero-photo" role="img" aria-label="Photo of a hand holding a stethoscope against a pale blue background"></div>
    <div class="benefits-panel">
      <ul class="benefits">
        <li>All training is by licensed healthcare providers.</li>
        <li>Courses meet State and OSHA requirements.</li>
        <li>Pricing is typically lower than having to get educated at yearly conferences.</li>
        <li>We use clean and full functioning equipment with the latest technology available.</li>
        <li>Training available at the business (easier for all employees cutting overall costs) and off site training.</li>
      </ul>
    </div>
  </section>

</main>
</body>
</html>
```